The Deskwell (A new and exciting small Business support solution) Business Cards

The Deskwell Business Card Design

About us:
The Deskwell is a small business support solution, assisting businesses with any marketing, office management and human resource skills.

Objective
To be a small business lifesaver, to relieve busy professionals from mundane operations so they can focus on their businesses future through complete, reliable, efficient and effective client support. To have people say WOW what did we do before The Deskwell.

Industry/Entity Type

Small Business

Colors
0355a3
33a6d7

Requirements
Must have
• Must be similar to the look and feel of my website http://www.thedeskwell.com.au/

Must have:

Blue colour is 0094FF

The Logo

A Small Business Support Solution
- Human Resources
- Office Administration
- Marketing

Marisa Holt
0487 302 615
marisaholt@thedeskwell.com.au
www.thedeskwell.com

```html
<!DOCTYPE html>
<html lang="en">
<head>
<meta charset="utf-8">
<title>The Deskwell — Business Card</title>
<link rel="stylesheet" href="https://fonts.googleapis.com/css2?family=Open+Sans:wght@400;600;700&display=swap">
<style>
  :root {
    --backdrop: #e8e6e3;
    --card: #ffffff;
    --navy: #0355a3;
    --ink: #111111;
    --text: #1a1a1a;
  }
  * { margin: 0; padding: 0; box-sizing: border-box; }
  html, body {
    width: 1200px;
    height: 970px;
    overflow: hidden;
    background: var(--backdrop);
    font-family: "Open Sans", Arial, sans-serif;
  }
  .business-card {
    position: absolute;
    left: 100px;
    top: 182px;
    width: 1000px;
    height: 606px;
    background: var(--card);
    box-shadow: 0 10px 30px rgba(0,0,0,0.12);
    overflow: hidden;
  }
  .holder-name {
    position: absolute;
    right: 68px;
    top: 66px;
    font-size: 26px;
    font-weight: 700;
    letter-spacing: 0.5px;
    color: var(--navy);
    line-height: 36px;
    text-transform: uppercase;
  }
  .name-tab {
    position: absolute;
    right: 0;
    top: 64px;
    width: 60px;
    height: 38px;
    background: var(--navy);
  }
  .wordmark {
    position: absolute;
    left: 0;
    right: 0;
    top: 220px;
    text-align: center;
    font-size: 124px;
    font-weight: 400;
    line-height: 150px;
    letter-spacing: -1px;
    color: var(--ink);
  }
  .contact-list {
    position: absolute;
    left: 62px;
    top: 474px;
    list-style: none;
  }
  .contact-item {
    display: flex;
    align-items: center;
    height: 37px;
    font-size: 17px;
    color: var(--text);
  }
  .contact-icon {
    width: 24px;
    height: 24px;
    margin-right: 10px;
    flex: none;
  }
  .service-list {
    position: absolute;
    left: 642px;
    top: 480px;
    list-style: none;
  }
  .service-item {
    font-size: 17px;
    line-height: 23px;
    color: var(--text);
  }
  .footer-band {
    position: absolute;
    left: 0;
    bottom: 0;
    width: 100%;
    height: 21px;
    background: var(--navy);
  }
</style>
</head>
<body>
  <div class="business-card">
    <div class="holder-name">Marisa Holt</div>
    <div class="name-tab"></div>

    <div class="wordmark">The Deskwell.</div>

    <ul class="contact-list">
      <li class="contact-item">
        <svg class="contact-icon" viewBox="0 0 24 24" aria-hidden="true">
          <rect x="1" y="1" width="22" height="22" rx="4" fill="var(--navy)"/>
          <path d="M8 5.5c.6-.4 1.4-.3 1.8.3l1.2 2c.3.6.2 1.2-.3 1.6l-.9.6c.6 1.6 1.8 3 3.3 3.9l.7-.8c.4-.5 1.1-.6 1.6-.2l1.9 1.3c.6.4.7 1.2.3 1.8l-.8 1c-.7.8-1.8 1.1-2.8.7-3.5-1.4-6-4.3-7-7.8-.3-1 .1-2 .9-2.6z" fill="#fff"/>
        </svg>
        0487 302 615
      </li>
      <li class="contact-item">
        <svg class="contact-icon" viewBox="0 0 24 24" aria-hidden="true">
          <rect x="2" y="5" width="20" height="14" fill="none" stroke="var(--navy)" stroke-width="2"/>
          <path d="M2.5 6l9.5 7 9.5-7" fill="none" stroke="var(--navy)" stroke-width="2"/>
        </svg>
        marisaholt@thedeskwell.com.au
      </li>
      <li class="contact-item">
        <svg class="contact-icon" viewBox="0 0 24 24" aria-hidden="true">
          <circle cx="11" cy="11" r="9" fill="none" stroke="var(--navy)" stroke-width="2"/>
          <ellipse cx="11" cy="11" rx="4" ry="9" fill="none" stroke="var(--navy)" stroke-width="1.6"/>
          <path d="M2 11h18M4 6h14M4 16h14" stroke="var(--navy)" stroke-width="1.6"/>
          <path d="M14 14l8 3-3.2 1.2L17.5 22z" fill="var(--navy)" stroke="#fff" stroke-width="1"/>
        </svg>
        www.thedeskwell.com
      </li>
    </ul>

    <ul class="service-list">
      <li class="service-item">- A Small Business Support Solution</li>
      <li class="service-item">- Human Resources</li>
      <li class="service-item">- Office Administration</li>
      <li class="service-item">- Marketing</li>
    </ul>

    <div class="footer-band"></div>
  </div>
</body>
</html>
```